Personal Card: Make it roar!

Hello to all designers,
Hope you're having a nice day/evening! Let's cut to the chase. I would like a modern, beautiful and professional personal business card; with a vector-art of a lion. I'd like the lion to be Blood Red. On a black background. I'm a Filipino, and would love to have my country's flag incorporated into the design. Id like the stars of my flag to be used in your designs if possible. The texts I want on the card are only my name, number, and email address. Colour of my name should be White, and my details Silver. The size and font should be simple and professional, you're in charge of that! The placements of the lion and my details will be yours to decide.

At the back of the card, I would like just the words "Thank You" (Silver) on a Black Background. Right on the center.

To summarise, my requirements are:
- Blood Red: Front Face of Lion, Vector-Art
- Black: Background
- Yellow: Three Stars used in the design
- White: Benedict Sr Talavera
- Silver: Number & Email (Where appropriate)
- Back of the card (Center). Silver: "Thank You"
- Please DON'T use the colour blue.

It's all about the Lion. Images you'll find attached are some images of Lions' faces which I particularly want to be captured and put onto the card. Convert it into a vector-art. A vector-art Lion. PLEASE use the images attached for inspiration only! Do not use it on your designs. Thank you very much for your time.

Good luck!

Ben
Updates

Hello Desginers, Please use Blood Red for the colour red in your designs:HEX: 8A0707RGB: 138,7,7Thank you,Ben Added Saturday, March 12, 2016

Target Market(s)

Potential Connections

Industry/Entity Type

It Professional

Contact Information for Business Card

Name: Benedict Sr Talavera
Email: bentalavera@mailhaven.co.uk
Number: 07382614927

Requirements
Must have
• Modern, Professional & Simple
• (Blood Red HEX: 8A0707, RGB: 138,7,7) Lion (Vector-style art)
• (Black) Background
• (White) My Name
• (Silver) My Details
• Back of card: "Thank You" in Silver. Font size should be small/medium.
• Only colours that should be used are Red, Black, Yellow and White/Silver
Nice to have
• - Use of 3 Yellow stars on the design
Should not have
• - Please avoid using any other colours apart from those specified.

```html
<!DOCTYPE html>
<html lang="en">
<head>
<meta charset="utf-8">
<title>Benedict Sr Talavera – Business Card</title>
<link rel="stylesheet" href="https://fonts.googleapis.com/css2?family=Open+Sans:wght@400;600&display=swap">
<style>
  :root {
    --page-bg: #e9e6e3;
    --card-black: #000000;
    --wave-red-top: #f22a00;
    --wave-red-bottom: #b8180a;
    --stripe-yellow: #f6ef7a;
    --star-yellow: #ede31c;
    --lion-red: #e8260a;
    --lion-red-deep: #b81a08;
    --name-white: #ffffff;
    --detail-silver: #f4f1ef;
  }
  * { margin: 0; padding: 0; box-sizing: border-box; }
  html, body {
    width: 1200px;
    height: 900px;
    overflow: hidden;
    background: var(--page-bg);
    font-family: "Open Sans", Arial, sans-serif;
  }
  .business-card {
    position: absolute;
    left: 80px;
    top: 128px;
    width: 1040px;
    height: 643px;
    background: var(--card-black);
    overflow: hidden;
    box-shadow: 0 14px 40px rgba(0,0,0,0.25);
  }
  .card-art {
    position: absolute;
    inset: 0;
    width: 1040px;
    height: 643px;
  }
  .lion-artwork {
    position: absolute;
    left: 105px;
    top: 80px;
    width: 350px;
    height: 362px;
    border-radius: 46% 40% 30% 38%;
    background: radial-gradient(circle at 40% 40%, var(--lion-red), var(--lion-red-deep));
  }
  .contact-block {
    position: absolute;
    right: 50px;
    top: 425px;
    text-align: right;
  }
  .holder-name {
    color: var(--name-white);
    font-weight: 600;
    font-size: 36px;
    line-height: 1;
    margin-bottom: 40px;
  }
  .detail-line {
    color: var(--detail-silver);
    font-weight: 400;
    font-size: 26px;
    line-height: 1;
    margin-bottom: 17px;
    display: flex;
    justify-content: flex-end;
    align-items: center;
    gap: 18px;
  }
  .detail-icon { width: 22px; height: 22px; flex: none; }
</style>
</head>
<body>
  <div class="business-card">
    <svg class="card-art" viewBox="0 0 1040 643" aria-hidden="true">
      <defs>
        <linearGradient id="waveRed" x1="0" y1="0" x2="0" y2="1">
          <stop offset="0" stop-color="var(--wave-red-top)"/>
          <stop offset="1" stop-color="var(--wave-red-bottom)"/>
        </linearGradient>
      </defs>
      <path class="wave-stripe" fill="var(--stripe-yellow)" transform="translate(0,-20)"
        d="M0,410 C120,470 220,540 330,535 C500,530 700,330 860,310 C950,300 1010,330 1040,350 L1040,643 L0,643 Z"/>
      <path class="wave-edge" fill="var(--card-black)" transform="translate(0,-9)"
        d="M0,410 C120,470 220,540 330,535 C500,530 700,330 860,310 C950,300 1010,330 1040,350 L1040,643 L0,643 Z"/>
      <path class="wave-red" fill="url(#waveRed)"
        d="M0,410 C120,470 220,540 330,535 C500,530 700,330 860,310 C950,300 1010,330 1040,350 L1040,643 L0,643 Z"/>
      <g class="flag-stars" fill="var(--star-yellow)">
        <polygon transform="translate(801,126) rotate(-8)" points="0,-36 8.5,-11.5 34,-11 13.5,4.5 21,29 0,14.5 -21,29 -13.5,4.5 -34,-11 -8.5,-11.5"/>
        <polygon transform="translate(952,126) rotate(8)" points="0,-36 8.5,-11.5 34,-11 13.5,4.5 21,29 0,14.5 -21,29 -13.5,4.5 -34,-11 -8.5,-11.5"/>
        <polygon transform="translate(876,206)" points="0,-36 8.5,-11.5 34,-11 13.5,4.5 21,29 0,14.5 -21,29 -13.5,4.5 -34,-11 -8.5,-11.5"/>
      </g>
    </svg>

    <div class="lion-artwork" role="img" aria-label="Red vector illustration of a lion's head in profile with a flowing mane"></div>

    <div class="contact-block">
      <p class="holder-name">Benedict Sr Talavera</p>
      <p class="detail-line">07382614927
        <svg class="detail-icon" viewBox="0 0 24 24" aria-hidden="true"><path fill="var(--detail-silver)" d="M6.6 10.8c1.4 2.8 3.8 5.1 6.6 6.6l2.2-2.2c.3-.3.7-.4 1-.2 1.1.4 2.3.6 3.6.6.6 0 1 .4 1 1V20c0 .6-.4 1-1 1C10.6 21 3 13.4 3 4c0-.6.4-1 1-1h3.5c.6 0 1 .4 1 1 0 1.3.2 2.5.6 3.6.1.3 0 .7-.2 1z"/></svg>
      </p>
      <p class="detail-line">bentalavera@mailhaven.co.uk
        <svg class="detail-icon" viewBox="0 0 24 24" aria-hidden="true"><rect x="2" y="5" width="20" height="14" fill="var(--detail-silver)"/><path d="M2 5l10 8 10-8" fill="none" stroke="#c21c08" stroke-width="1.6"/></svg>
      </p>
    </div>
  </div>
</body>
</html>
```